Banner Ads Design Project

We need 3 new banner ads designed for the front page of our website. If you navigate to www.brightvane.net.au you will see there is a banner ad slider just underneath the menu at the top and we require 3 new designs created.
You will see that there is some text overlay at the right of the image, which is editable via our content management system. The background image therefore needs to be white in that area or at least very light as text will sit on top.
The image dimension is 940 x 335 and has beveled edges.
The 3 designs we require are as follows (note we don't just want to use pictures, we want more specific and custom designs created):
Desgin 1 - Radio Ad Link
BrightVane is currently running a radio campaign with Wave 94.7. We would like to advertise this on our website. See http://www.wave947.fm/win/cover-the-rent for an example of what we are after.
Design 2 - Special on LED's
We are running a special on LED lights at the moment. We need a design that includes an image of our LED light, which is attached. But also with some nice design elements, not just a picture of the light. I have attached a flyer we use for inspiration.
Design 3 - We want to advertise our new office in mitchell. So am simply after an image created using the attached photo of our office. That obviously has some white space at the right hand side so that I can overlay text.
Thanks,
Karl

```html
<!DOCTYPE html>
<html lang="en">
<head>
<meta charset="utf-8">
<title>BrightVane – Canberra's Energy Saving Specialists</title>
<link href="https://fonts.googleapis.com/css2?family=PT+Sans:wght@400;700&family=Arimo:wght@400;700&family=Caveat:wght@500&display=swap" rel="stylesheet">
<style>
:root{
  --green-top:#b2c80c;
  --green-bottom:#5e8a22;
  --green-dark:#6a8a2c;
  --navy:#2f3b77;
  --navy-mid:#3f4c87;
  --form-bg:#46548a;
  --body-text:#6a6a6a;
  --link:#2f3f8a;
  --rule:#d6d6d6;
  --page:#ffffff;
}
*{box-sizing:border-box;margin:0;padding:0}
html,body{width:1200px;height:1000px;overflow:hidden;background:var(--page)}
body{position:relative;font-family:Arimo,Arial,sans-serif;color:var(--body-text)}
.abs{position:absolute}
.page-band{left:0;top:0;width:1200px;height:405px;background:linear-gradient(#ececec 0,#fff 60px,#fff 160px,#f1f1f1 260px,#e6e6e6 405px)}
.top-rule{left:0;top:0;width:1200px;height:5px;background:var(--green-dark)}
.consult-tab{left:737px;top:0;width:286px;height:27px;background:var(--green-dark);border-radius:0 0 5px 5px;color:#fff;font-size:12px;line-height:27px;text-align:center}
.consult-tab b{font-weight:700}
.consult-tab .tab-link{color:#f2d21b}
.brand-dot{left:254px;top:34px;width:56px;height:56px;border-radius:50%;background:var(--green-bottom)}
.brand-name{left:218px;top:92px;font-family:"PT Sans",sans-serif;font-weight:700;font-size:27px;line-height:32px;color:var(--navy);letter-spacing:-0.5px}
.tagline{left:357px;top:104px;font-family:Caveat,cursive;font-size:20px;line-height:24px;color:#555}
.login-title{left:638px;top:60px;font-size:10px;font-weight:700;color:#444;letter-spacing:.3px}
.login-status{left:828px;top:60px;font-size:11px;color:#777}
.login-status a{color:var(--link);text-decoration:none}
.login-box{left:625px;top:78px;width:398px;height:47px;background:#e4e4e4;border-radius:6px}
.field{position:absolute;height:24px;background:#fff;border:1px solid #c8c8c8;border-radius:2px;font-size:12px;color:#999;padding-left:9px;line-height:22px}
.login-btn{left:963px;top:89px;width:46px;height:24px;background:linear-gradient(#5a69a6,#34427e);border-radius:2px;color:#fff;font-size:11px;font-weight:700;text-align:center;line-height:24px}
.main-nav{left:184px;top:155px;width:839px;height:42px;background:linear-gradient(var(--green-top),var(--green-bottom));border-radius:4px;box-shadow:0 2px 3px rgba(0,0,0,.2);display:flex;padding-left:11px}
.main-nav span{font-family:"PT Sans",sans-serif;font-weight:700;font-size:11px;color:#fff;line-height:42px;padding:0 12.5px;letter-spacing:.4px}
.banner{left:183px;top:210px;width:840px;height:300px;border-radius:3px;overflow:hidden;box-shadow:0 3px 5px rgba(0,0,0,.12)}
.banner-photo{left:0;top:0;width:535px;height:300px;background:linear-gradient(135deg,#dde4ea,#b9c8a6)}
.banner-side{left:535px;top:0;width:305px;height:300px;background:linear-gradient(160deg,#f5f7fa,#e6ebf2 60%,#eef1f6)}
.banner-prev{left:516px;top:113px}
.banner-title{left:582px;top:58px;font-family:Arimo,sans-serif;font-weight:700;font-size:27px;line-height:31px;color:var(--navy)}
.banner-copy{left:582px;top:137px;width:209px;font-size:11px;line-height:12.4px;color:#111}
.btn{position:absolute;color:#fff;font-size:10px;text-align:center;border-radius:2px}
.btn-blue{background:linear-gradient(#5867a6,#33417c)}
.btn-green{background:linear-gradient(#a6c114,#5c8721)}
.section-title{position:absolute;font-family:"PT Sans",sans-serif;font-weight:700;font-size:14px;line-height:16px;color:var(--navy-mid);letter-spacing:.4px}
.col-text{position:absolute;width:270px;font-size:11px;line-height:16px;color:var(--body-text)}
.col-text p+p{margin-top:16px}
.col-text a{color:var(--link);text-decoration:none}
.consult-form{left:755px;top:563px;width:268px;height:261px;background:var(--form-bg);border-radius:4px}
.form-intro{left:16px;top:24px;width:230px;font-size:11px;line-height:16px;color:#fff}
.form-label{position:absolute;left:16px;font-size:11px;color:#fff}
.footer-rule{left:0;top:881px;width:1200px;height:3px;background:var(--navy-mid)}
.footer-col{position:absolute;top:892px;width:155px}
.footer-col h4{font-family:"PT Sans",sans-serif;font-weight:700;font-size:13px;line-height:16px;color:var(--navy-mid);letter-spacing:.3px;padding-bottom:6px;border-bottom:1px solid var(--rule)}
.footer-col ul{list-style:none;margin-top:5px}
.footer-col li{font-size:11px;line-height:17px;color:#555}
.footer-col .sub{font-weight:700;margin-top:2px}
</style>
</head>
<body>
<div class="abs page-band"></div>
<div class="abs top-rule"></div>
<div class="abs consult-tab"><b>FREE Consultation</b> 1300 486 705 | <span class="tab-link">Contact Us</span></div>

<div class="abs brand-dot"></div>
<div class="abs brand-name">brightvane</div>
<div class="abs tagline">Canberra's Energy Saving Specialists</div>

<div class="abs login-title">LOGIN TO BRIGHTVANE</div>
<div class="abs login-status">No one logged in. <a>My Account</a> | <a>Register</a></div>
<div class="abs login-box"></div>
<div class="field" style="left:638px;top:89px;width:160px">username</div>
<div class="field" style="left:800px;top:89px;width:160px">••••••••</div>
<div class="abs login-btn">Login</div>

<nav class="abs main-nav">
  <span>SOLAR PANELS</span><span>SOLAR HOT WATER</span><span>LED LIGHTING</span><span>ENERGY EFFICIENCY</span><span>REAL-TIME MONITORING</span><span>FREE CONSULTATION</span><span>BLOG</span>
</nav>

<section class="abs banner">
  <div class="abs banner-photo" role="img" aria-label="Product photo: LED downlight in a solar field setting"></div>
  <div class="abs banner-side" role="img" aria-label="Faint solar panels fading to white behind the text"></div>
  <svg class="abs banner-prev" width="38" height="38" viewBox="0 0 38 38">
    <circle cx="19" cy="19" r="17" fill="#fff" stroke="#c8ccd4" stroke-width="2"/>
    <circle cx="19" cy="19" r="12" fill="#eef0f4"/>
    <path d="M21 13 L15 19 L21 25" fill="none" stroke="#3a4676" stroke-width="3" stroke-linecap="round" stroke-linejoin="round"/>
  </svg>
  <h1 class="abs banner-title">Special<br>on LED's</h1>
  <p class="abs banner-copy">We are running a special on LED lights at the moment. We need a design that includes an image of our LED light, which is attached. But also with some nice design elements, not just a picture of the light. I have attached a flyer we use for inspiration.</p>
  <div class="btn btn-blue" style="left:584px;top:239px;width:92px;height:24px;line-height:24px">Get Started</div>
</section>

<h2 class="section-title" style="left:182px;top:537px">SOLAR PANELS CANBERRA</h2>
<div class="col-text" style="left:182px;top:563px">
  <p>Looking for a great quality Solar Energy System for your home or business? BrightVane offers a range of systems to suit your requirements and budget and only use top quality components from reputable brands such as Voltrek and Helion.</p>
  <p>BrightVane is a local company that focuses on its customers with a dedicated account manager for every customer from start to finish. We have being installing systems in Canberra and the surrounding region for over 2 years and pride ourselves on the quality of our workmanship and timeliness of our installs.</p>
</div>
<div class="btn btn-green" style="left:333px;top:772px;width:118px;height:26px;line-height:26px">Browse Systems</div>

<h2 class="section-title" style="left:468px;top:537px">SOLAR ENERGY MONITORING</h2>
<div class="col-text" style="left:468px;top:563px">
  <p>If you purchase a Solar Energy System greater than 3kW you will receive energy monitoring equipment for free. This equipment will provide real-time data that will tell you how much energy you are consuming and generating at any time of day.</p>
  <p>We believe in building systems with out perform our competitors and have the data to provide it. Browse through our VaneMap to see how systems in your area are performing or how your usage compares to others. <a>Click here</a> to see and example of a system in Wanniassa, Canberra.</p>
</div>
<div class="btn btn-green" style="left:652px;top:772px;width:85px;height:26px;line-height:26px">View Map</div>

<h2 class="section-title" style="left:755px;top:537px">GET A FREE CONSULTATION</h2>
<form class="abs consult-form">
  <p class="abs form-intro">Fill in your details below and one of our consultants will contact you to discuss our products and services</p>
  <span class="form-label" style="top:93px">First Name</span>
  <span class="form-label" style="top:127px">Last Name</span>
  <span class="form-label" style="top:161px">Phone No.</span>
  <span class="form-label" style="top:195px">Email</span>
  <div class="field" style="left:114px;top:82px;width:138px;height:25px">first name</div>
  <div class="field" style="left:114px;top:116px;width:138px;height:25px">last name</div>
  <div class="field" style="left:114px;top:150px;width:138px;height:25px">tel number</div>
  <div class="field" style="left:114px;top:184px;width:138px;height:25px">e-mail address</div>
  <div class="btn btn-green" style="left:39px;top:218px;width:139px;height:24px;line-height:24px;font-weight:700;font-size:11px">Get a Free Consultation</div>
</form>

<div class="abs footer-rule"></div>
<div class="footer-col" style="left:182px"><h4>SOLAR PANELS</h4><ul><li>Solar Panels Canberra</li><li>Solar Panels NSW</li><li>How do Solar Energy Systems work?</li><li>The benefits of Solar Energy</li></ul></div>
<div class="footer-col" style="left:346px"><h4>SOLAR HOT WATER</h4><ul><li>Solar Hot Water Canberra</li><li>How does Solar Hot Water work?</li><li>Government Rebates</li><li>Switching to a Solar Hot Water</li></ul></div>
<div class="footer-col" style="left:510px"><h4>LED LIGHTING</h4><ul><li>Online Shop</li><li>About LED Lighting</li><li>Make the Switch from Globe to LED Lighting</li><li>Are Photovoltaic Systems</li></ul></div>
<div class="footer-col" style="left:674px"><h4>REAL-TIME MONITORING</h4><ul><li>Browse Map</li><li>Register my system</li><li>Key Statistics</li><li>FAQ's</li></ul></div>
<div class="footer-col" style="left:838px"><h4>CONTACT US</h4><ul><li>Free Consultation</li><li>Tel: 1300 486 705</li><li>Fax: 02 6044 2918</li><li class="sub">Office Address</li><li>2/7 Carrow St</li></ul></div>
</body>
</html>
```